Looking for a cool, modern Cannabis Jar Label

I want you to come up with a better, modern look for a label.

I need it sized to 4” x 3” - I plan to print directly to label printer.

I want you to use Photoshop and deliver me a layered PSD file that I can edit and modify the information as needed..

The label information will need to include places for:
(1) Strain Name - most important part of label - larger font size than rest - example Marlow Frost, KTV #7, Copperleaf Haze
(2) Pricing - for Gram, 1/8, 1/4, 1/2. and Ounce
(3) Strain Designation (Hybrid, Indica or Sativa) - maybe color coded, different color for Indica v. Sativa, just an idea
(4) THC and CBD percentages - for example 23% THC and 0.05% CBD
(5) Farm name - a place where we can add the name/logo of the business that produced the product. example - Bramwell Farms

I have attached a simple mockup showing the information.

I have also attached a few samples of labels we like to give you an idea of the look and feel we are going for.

I am wanting a very clean, modern, classy, readable look.The font will use is Gotham Font.

HI Everyone! Thank you for all of your designs. I am requesting an extension because I need more time to give adequate feedback to the designers. Thank you for your participation and all of your efforts! I will be making a decision soon!

• Gotham Font

Designer to choose colors to be used in the design.

• Thank you for your designs. I am sorry i have been slow in providing feedback, things have been really busy around here!
• I wanted to give some group general feedback. After reviewing all of the designs, there is a common theme among all of the designs that I would like to see changed.
• I would like to see the per gram pricing more prominent on the label. This is what most people are looking for when they are purchasing the product. So I would like to see this stand out from the other pricing tiers. As I think about it, they don't all need to be grouped together in a line. You could have the Per Gram pricing front and center some where and then the other pricing tiers grouped together somewhere else on the label.
• This is the order of importance of items on the label. Items at the the top of the list should be bigger than those below it.
• 1. Strain name
• 2. Pricing - being per gram the most important of all prices
• 3. THC/CBD percentages
• 4. Strain Type (indica, sativa, hybrid)
• 5. Farm name/logo
• When laying out these labels, they will be going on rounded jars and they will be on display. Think of jars with fancy labels in a candy store. They need to be eye catchy, appealing, but easy read.
• Thank you for all of your hard work, everyone is doing a great job.
• Best,
• Nadia

```html
<!DOCTYPE html>
<html lang="en">
<head>
<meta charset="utf-8">
<title>Marlow Frost – Jar Label</title>
<link rel="stylesheet" href="https://fonts.googleapis.com/css2?family=Montserrat:wght@400;500;700&family=Pathway+Gothic+One&display=swap">
<style>
  :root {
    --backdrop: #4d4d4d;
    --label: #ffffff;
    --leaf-green: #1a6b30;
    --ink: #000000;
    --muted: #5a5a5a;
  }
  html, body {
    margin: 0;
    padding: 0;
    width: 1200px;
    height: 1200px;
    overflow: hidden;
    background: var(--backdrop);
  }
  .canvas {
    position: relative;
    width: 1200px;
    height: 1200px;
    background: var(--backdrop);
    font-family: "Montserrat", sans-serif;
    color: var(--ink);
  }
  .jar-label {
    position: absolute;
    left: 110px;
    top: 232px;
    width: 980px;
    height: 736px;
    background: var(--label);
  }
  .strain-frame {
    position: absolute;
    left: 24px;
    top: 17px;
    width: 931px;
    height: 241px;
    box-sizing: border-box;
    border: 7px solid var(--leaf-green);
    border-radius: 48px;
    display: flex;
    align-items: center;
    justify-content: center;
  }
  .strain-name {
    margin: 0;
    font-weight: 400;
    font-size: 92px;
    letter-spacing: 1px;
    line-height: 1;
    transform: translateY(-12px);
  }
  .strain-type {
    position: absolute;
    left: 363px;
    top: 240px;
    width: 254px;
    height: 54px;
    background: var(--leaf-green);
    border-radius: 0 0 10px 10px;
    color: var(--label);
    font-size: 38px;
    font-weight: 400;
    letter-spacing: 2px;
    display: flex;
    align-items: center;
    justify-content: center;
  }
  .price-list {
    position: absolute;
    left: 0;
    top: 352px;
    width: 980px;
    height: 110px;
    margin: 0;
    padding: 0;
    list-style: none;
  }
  .price-tier {
    position: absolute;
    top: 0;
    width: 190px;
    margin-left: -95px;
    text-align: center;
  }
  .price-amount {
    display: block;
    font-family: "Pathway Gothic One", sans-serif;
    font-size: 68px;
    line-height: 70px;
    white-space: nowrap;
  }
  .price-amount sup {
    font-size: 32px;
    vertical-align: 0;
    position: relative;
    top: -24px;
  }
  .price-unit {
    display: block;
    margin-top: -2px;
    font-size: 27px;
    color: var(--muted);
  }
  .potency-box {
    position: absolute;
    left: 32px;
    top: 508px;
    width: 337px;
    height: 209px;
    box-sizing: border-box;
    border: 4px solid var(--leaf-green);
  }
  .potency {
    position: absolute;
    top: 0;
    width: 154px;
    height: 205px;
  }
  .potency-thc { left: 0; }
  .potency-cbd { left: 178px; }
  .potency-value {
    position: absolute;
    left: 0;
    right: 0;
    top: 28px;
    text-align: center;
    font-family: "Pathway Gothic One", sans-serif;
    font-size: 94px;
    line-height: 94px;
  }
  .potency-value small {
    font-size: 44px;
  }
  .potency-tag {
    position: absolute;
    left: 0;
    bottom: 6px;
    width: 154px;
    height: 54px;
    background: var(--ink);
    color: var(--label);
    font-size: 38px;
    letter-spacing: 1px;
    display: flex;
    align-items: center;
    justify-content: center;
  }
  .potency-thc .potency-tag { border-radius: 0 12px 12px 0; left: -2px; }
  .potency-cbd .potency-tag { border-radius: 12px 0 0 12px; width: 152px; }
  .grower {
    position: absolute;
    left: 384px;
    top: 510px;
    width: 564px;
    height: 206px;
    border-top: 1.5px solid var(--ink);
    border-bottom: 1.5px solid var(--ink);
    text-align: center;
  }
  .grower-kicker {
    margin: 10px 0 0;
    font-weight: 700;
    font-size: 23px;
  }
  .grower-credit {
    margin: 2px 0 0;
    font-weight: 400;
    font-size: 20px;
  }
  .farm-name {
    display: block;
    margin-top: 38px;
    font-size: 44px;
    font-weight: 500;
    color: var(--ink);
    letter-spacing: 1px;
  }
</style>
</head>
<body>
<main class="canvas">
  <article class="jar-label">
    <header class="strain-frame">
      <h1 class="strain-name">Marlow Frost</h1>
    </header>
    <div class="strain-type">INDICA</div>

    <ul class="price-list">
      <li class="price-tier" style="left:100px"><span class="price-amount">€ 10<sup>.50</sup></span><span class="price-unit">Gram</span></li>
      <li class="price-tier" style="left:292px"><span class="price-amount">€ 35<sup>.00</sup></span><span class="price-unit">1/8</span></li>
      <li class="price-tier" style="left:480px"><span class="price-amount">€ 70<sup>.00</sup></span><span class="price-unit">1/4</span></li>
      <li class="price-tier" style="left:676px"><span class="price-amount">€ 140<sup>.00</sup></span><span class="price-unit">1/2</span></li>
      <li class="price-tier" style="left:868px"><span class="price-amount">€ 280<sup>.00</sup></span><span class="price-unit">Ounce</span></li>
    </ul>

    <section class="potency-box">
      <div class="potency potency-thc">
        <div class="potency-value">23<small>%</small></div>
        <div class="potency-tag">THC</div>
      </div>
      <div class="potency potency-cbd">
        <div class="potency-value">0.5<small>%</small></div>
        <div class="potency-tag">CBD</div>
      </div>
    </section>

    <footer class="grower">
      <p class="grower-kicker">Cannabis Flower</p>
      <p class="grower-credit">Cultivated By:</p>
      <span class="farm-name">Ashby Fields</span>
    </footer>
  </article>
</main>
</body>
</html>
```